IT Tradingsystem for car dealers needs Business Card Design

We need a fresh and modern design for our new business cards.

We develop a it-business system for car dealers in Sweden, Norway and on our way down to further countries in Europe, hence the namechange to BrolaTek Europe AB. The site can be found at www.brolatek-example.com. The startpage is also in for an update/modernization soon so don't take to much from here.

We are looking to print double sided, 4-colour cards.

We want to look professional, modern and serious. Open to cooler suggestions, but not too crazy. We need to make a good and serious impression on our potential customers. It needs to reflect our scandinavian design values and layout.

Preferably with the full BrolaTek logo in good size on the back, so the small print on the logo can be read easily.

Text that needs to go on the cards:
-------

Per Oskar Fjellström
Founder

Direct +46 70-512 96 47
Support 08-612 57 394
po.fjellstrom@brolatek-example.com

BrolaTek Europe AB
Box 8617
104 29 Stockholm

Brolatek-example.com
Saljportalen-example.se

--------
Good luck and thanks!

PS. If you need more input or see what our previous cards looked like, don't hesitate to contact me!

Target Market(s)

Decision makers / executives at brand cardealers

Industry/Entity Type

Automotive

Contact Information for Business Card

Normal size

Requirements
Must have
• Full logo
Nice to have
• Base on our orange colors
Should not have
• No fonts with serif, and not too much graphics

```html
<!DOCTYPE html>
<html lang="sv">
<head>
<meta charset="utf-8">
<title>BrolaTek – Business Card</title>
<link rel="stylesheet" href="https://fonts.googleapis.com/css2?family=Arimo:wght@400;700&family=Roboto+Condensed:wght@400;700&display=swap">
<style>
  :root {
    --bg: #1e1e1e;
    --card: #ffffff;
    --ink: #111111;
    --orange: #d98a22;
    --orange-light: #ecb56a;
    --band-text: #ffffff;
  }
  * { margin: 0; padding: 0; box-sizing: border-box; }
  html, body { width: 1200px; height: 801px; overflow: hidden; background: var(--bg); }
  .canvas {
    width: 1200px; height: 801px;
    display: flex; align-items: center; justify-content: center; gap: 60px;
  }
  .card {
    position: relative;
    width: 510px; height: 292px;
    background: var(--card);
    overflow: hidden;
    font-family: "Arimo", Arial, sans-serif;
    color: var(--ink);
  }
  .band {
    position: absolute; left: 0; right: 0; bottom: 0;
    height: 34px;
    background: var(--orange);
    border-top: 4px solid var(--orange-light);
    display: flex; align-items: center; justify-content: flex-end;
    padding-right: 26px;
    color: var(--band-text);
    font-size: 15px; letter-spacing: 0.04em;
  }
  .logo { display: flex; align-items: center; gap: 10px; }
  .logo-mark { width: 30px; height: 30px; background: var(--orange); flex: none; }
  .logo-name { font-weight: 700; font-size: 40px; letter-spacing: -0.01em; line-height: 1; }
  .tagline { font-size: 12px; margin-top: 4px; padding-left: 40px; }

  /* Contact side */
  .contact .logo { position: absolute; left: 30px; top: 36px; }
  .contact .tagline { position: absolute; left: 30px; top: 78px; }
  .person {
    position: absolute; left: 30px; top: 130px;
    font-family: "Roboto Condensed", Arial, sans-serif;
    font-size: 13px; line-height: 1.3;
  }
  .person-name { font-weight: 700; font-size: 15px; }
  .details { margin-top: 12px; }

  /* Logo side */
  .brand .logo { position: absolute; left: 40px; top: 90px; }
  .brand .logo-mark { width: 46px; height: 46px; }
  .brand .logo-name { font-size: 58px; }
  .brand .tagline { position: absolute; left: 40px; top: 152px; font-size: 15px; padding-left: 56px; letter-spacing: 0.03em; }
</style>
</head>
<body>
<main class="canvas">
  <section class="card contact">
    <div class="logo"><span class="logo-mark"></span><span class="logo-name">BrolaTek</span></div>
    <p class="tagline">VagnTest | Remarketing | saljportalen-example.se</p>
    <div class="person">
      <p class="person-name">Per Oskar Fjellström</p>
      <p>Founder</p>
      <div class="details">
        <p>BrolaTek Europe AB, Box 8617, 104 29 Stockholm</p>
        <p>Direct +46 70-512 96 47</p>
        <p>Support 08-612 57 394</p>
        <p>po.fjellstrom@brolatek-example.com</p>
      </div>
    </div>
    <div class="band">Brolatek-example.com • Saljportalen-example.se</div>
  </section>

  <section class="card brand">
    <div class="logo"><span class="logo-mark"></span><span class="logo-name">BrolaTek</span></div>
    <p class="tagline">VagnTest | Remarketing | saljportalen-example.se</p>
    <div class="band">Brolatek-example.com • Saljportalen-example.se</div>
  </section>
</main>
</body>
</html>
```